Rock Concert Ticket

Invitation for a 50th birthday party in the form of a ticket to a rock concert -
think Knives 'n Tulips, OX/EV, Tumbling Pebbles, The Brawl, Tin Balloon etc.
Design should be very rock n roll with album cover type feel. Needs to reference 50 and include information like venue, date, dress code, rsvp etc. Invitation to be distributed electronically rather than hard copy.

Reason: Deadline has been extended to allow for some slight changes to 2-3 of the designs that I have narrowed it down to. I contacted the designers directly with feedback so you know who you are. Thanks

```html
<!DOCTYPE html>
<html lang="en">
<head>
<meta charset="utf-8">
<title>Vince Turns Fifty – Rock Night Invitation</title>
<link href="https://fonts.googleapis.com/css2?family=Oswald:wght@300;400&family=Permanent+Marker&family=Share+Tech+Mono&display=swap" rel="stylesheet">
<style>
  :root {
    --ink-night: #1c1c1c;
    --ink-stub: #2b2b2b;
    --panel-black: #0c0c0c;
    --paper-white: #f4f4f4;
    --title-grey: #cfcfcf;
    --title-shade: #9a9a9a;
    --banner-cream: #e4dcaa;
    --banner-ink: #151515;
    --rose-red: #a3121a;
    --rose-deep: #4a0a0e;
    --leaf-dark: #3a3e30;
    --stub-text: #dcdcdc;
    --perforation: #d8d0a0;
  }
  * { margin: 0; padding: 0; box-sizing: border-box; }
  html, body { width: 1200px; height: 2880px; overflow: hidden; background: var(--ink-night); }
  .ticket {
    position: relative; width: 1200px; height: 2880px; overflow: hidden;
    background: linear-gradient(var(--ink-night) 0 2412px, var(--ink-stub) 2412px 100%);
  }
  .artwork { position: absolute; }
  .artwork--crest {
    left: 0; top: 0; width: 1200px; height: 880px;
    background:
      radial-gradient(ellipse 280px 300px at 820px 330px, rgba(210,210,210,.5), transparent 70%),
      radial-gradient(ellipse 220px 200px at 250px 500px, rgba(163,18,26,.85), transparent 70%),
      radial-gradient(ellipse 260px 200px at 620px 720px, rgba(163,18,26,.8), transparent 70%),
      radial-gradient(ellipse 160px 140px at 300px 120px, rgba(163,18,26,.6), transparent 70%);
  }
  .artwork--roses {
    left: 0; top: 1000px; width: 1200px; height: 1390px;
    background:
      radial-gradient(ellipse 260px 200px at 180px 140px, var(--rose-red), transparent 72%),
      radial-gradient(ellipse 260px 200px at 1020px 140px, var(--rose-red), transparent 72%),
      radial-gradient(ellipse 220px 260px at 140px 500px, var(--leaf-dark), transparent 72%),
      radial-gradient(ellipse 220px 260px at 1060px 500px, var(--leaf-dark), transparent 72%),
      radial-gradient(ellipse 260px 320px at 170px 960px, var(--rose-red), transparent 72%),
      radial-gradient(ellipse 260px 320px at 1030px 960px, var(--rose-red), transparent 72%),
      radial-gradient(ellipse 200px 160px at 140px 1300px, var(--rose-deep), transparent 72%),
      radial-gradient(ellipse 200px 160px at 1060px 1300px, var(--rose-deep), transparent 72%);
  }
  .headline {
    position: absolute; left: 0; width: 1200px; text-align: center; white-space: nowrap;
    font-family: "Oswald", sans-serif; color: var(--title-grey);
    background: linear-gradient(var(--paper-white), var(--title-shade));
    -webkit-background-clip: text; background-clip: text; -webkit-text-fill-color: transparent;
  }
  .headline__name { top: -33px; font-size: 380px; font-weight: 400; line-height: 1; transform: scaleX(.64); }
  .headline__turns {
    top: 384px; left: 408px; width: 372px; font-size: 89px; font-weight: 300; line-height: 93px;
    border-top: 10px solid var(--paper-white); border-bottom: 10px solid var(--paper-white);
  }
  .headline__age { top: 493px; font-size: 311px; font-weight: 400; line-height: 1; transform: scaleX(.86); }
  .banner {
    position: absolute; left: 72px; top: 808px; width: 1032px; height: 172px;
    background: var(--banner-cream); transform: rotate(1.5deg);
    display: flex; align-items: center; justify-content: center; white-space: nowrap;
    font-family: "Permanent Marker", Impact, sans-serif; font-size: 60px; color: var(--banner-ink);
  }
  .star { position: absolute; left: 556px; top: 1048px; width: 88px; height: 88px; }
  .details {
    position: absolute; left: 216px; top: 1152px; width: 768px; height: 1212px;
    background: var(--panel-black); color: var(--paper-white);
    font-family: "Share Tech Mono", monospace; font-size: 58px; line-height: 80px; text-align: center;
  }
  .details__block { position: absolute; left: 0; width: 100%; white-space: nowrap; }
  .details__rule { position: absolute; left: 0; width: 100%; height: 12px; background: var(--paper-white); }
  .stub {
    position: absolute; left: 0; top: 2406px; width: 1200px; height: 474px;
    border-top: 8px dotted var(--perforation);
    font-family: "Share Tech Mono", monospace; font-size: 54px; letter-spacing: 6px; color: var(--stub-text); text-align: center;
  }
  .stub__line { position: absolute; left: 0; width: 100%; line-height: 70px; white-space: nowrap; }
  .stub__reply { word-spacing: 60px; }
</style>
</head>
<body>
<main class="ticket">
  <div class="artwork artwork--crest" role="img" aria-label="Illustration of red roses on thorny stems around a grey skull with white flowers"></div>
  <div class="artwork artwork--roses" role="img" aria-label="Illustration of large red roses and dark green leaves framing the details panel"></div>

  <h1 class="headline headline__name">VINCE</h1>
  <p class="headline headline__turns">TURNS</p>
  <p class="headline headline__age">FIFTY</p>

  <p class="banner">ROCK ALL NIGHT TILL THE END</p>

  <svg class="star" viewBox="0 0 100 100" aria-hidden="true"><polygon fill="#f4f4f4" points="50,4 62,38 98,38 69,60 80,95 50,74 20,95 31,60 2,38 38,38"/></svg>

  <section class="details">
    <p class="details__block" style="top:28px">NOVEMBER 14, 2014</p>
    <p class="details__block" style="top:152px">VELVET AMP BAR<br>48 CINDER STREET,<br>ASHFORD, CR 2047</p>
    <div class="details__rule" style="top:426px"></div>
    <p class="details__block" style="top:470px">COCKTAILS AT 6P,<br>DINNER AT 7PM</p>
    <div class="details__rule" style="top:666px"></div>
    <p class="details__block" style="top:710px">NOSTALGIZING 'N'<br>ROCKIN' 'N' ROLLIN'<br>TILL 12 MIDNIGHT</p>
    <div class="details__rule" style="top:974px"></div>
    <p class="details__block" style="top:1022px">NADIA REYES<br>(555) 284.6173</p>
  </section>

  <footer class="stub">
    <p class="stub__line" style="top:25px">VALID FOR ONE NIGHT ONLY</p>
    <p class="stub__line" style="top:126px">RESPOND BEFORE NOV. 8</p>
    <p class="stub__line stub__reply" style="top:217px">____ACCEPTS ____REJECTS</p>
    <p class="stub__line" style="top:337px">NUMBERS ATTENDING ____</p>
  </footer>
</main>
</body>
</html>
```